Mox Dune Reel Business cards

Logo, tag line and photo on card
Agent Name
Title
Address
Phone number
Email
Website
Make logo on one side large by rotating  to portrait format.  Keep the background of the logo white.

Contact Information for Business Card
Slogan; Shaping Every Mox Ahead

```html
<!DOCTYPE html>
<html lang="en">
<head>
<meta charset="utf-8">
<title>Mox Dune Reel Business Cards</title>
<link rel="stylesheet" href="https://fonts.googleapis.com/css2?family=Montserrat:wght@400;500;600;700;800&display=swap">
<style>
  :root {
    --navy: #24336e;
    --navy-light: #33458a;
    --red: #d0262d;
    --white: #ffffff;
    --backdrop: #b3b4b6;
    --photo-a: #cfcfd1;
    --photo-b: #6b6a6c;
  }
  * { box-sizing: border-box; margin: 0; padding: 0; }
  html, body {
    width: 1200px; height: 781px; overflow: hidden;
    background: var(--backdrop);
    font-family: "Montserrat", sans-serif;
  }
  .stage {
    position: relative; width: 1200px; height: 781px;
    display: flex; justify-content: center; align-items: center; gap: 90px;
  }
  .card {
    width: 360px; height: 630px; border-radius: 26px;
    position: relative; overflow: hidden;
    box-shadow: 0 10px 26px rgba(0,0,0,0.18);
  }
  /* Front: contact side */
  .card--front {
    background: linear-gradient(160deg, var(--navy) 0%, var(--navy) 55%, var(--navy-light) 100%);
    color: var(--white);
    display: flex; flex-direction: column; align-items: center;
    padding-top: 44px;
  }
  .portrait-frame {
    width: 252px; height: 252px; border-radius: 30px;
    border: 7px solid var(--red); background: var(--white);
    overflow: hidden; display: flex; align-items: flex-end; justify-content: center;
  }
  .portrait {
    width: 100%; height: 100%;
    background: radial-gradient(ellipse at 50% 40%, var(--photo-a) 0%, var(--photo-b) 75%);
  }
  .agent-name {
    margin-top: 30px; font-weight: 800; font-size: 25px; letter-spacing: 0.5px;
    text-transform: uppercase;
  }
  .agent-title {
    margin-top: 2px; font-weight: 500; font-size: 17px; color: var(--red);
  }
  .address {
    margin-top: 22px; text-align: center; font-size: 15px; line-height: 1.45; font-weight: 500;
  }
  .contact-icons {
    margin-top: 22px; display: flex; gap: 10px;
  }
  .contact-icons svg { width: 16px; height: 16px; }
  .contact-list {
    margin-top: 14px; list-style: none; text-align: center;
    font-size: 15px; line-height: 1.55; font-weight: 500;
  }
  .contact-list .phone { letter-spacing: 3px; font-size: 16px; }

  /* Back: brand side */
  .card--back {
    background: var(--white);
    display: flex; flex-direction: column; align-items: center;
  }
  .brand {
    margin-top: 150px; display: flex; flex-direction: column; align-items: center;
  }
  .brand-mark {
    width: 26px; height: 26px; background: var(--red); margin-bottom: 22px;
  }
  .brand-name {
    color: var(--navy); font-weight: 800; font-size: 68px; line-height: 0.98;
    text-align: center; letter-spacing: -1px;
  }
  .tagline {
    position: absolute; bottom: 48px; left: 0; right: 0; text-align: center;
    color: var(--navy); font-weight: 600; font-size: 17px; letter-spacing: 0.3px;
  }
</style>
</head>
<body>
<main class="stage">
  <section class="card card--front" aria-label="Business card, contact side">
    <div class="portrait-frame">
      <div class="portrait" role="img" aria-label="Portrait photo of the founder, smiling, in a patterned shirt"></div>
    </div>
    <h1 class="agent-name">Marcus Hale</h1>
    <p class="agent-title">Founder</p>
    <p class="address">Suite 1200, 250 - 5th Street<br>NW, Ridgeford, AB, T3K 2L8</p>
    <div class="contact-icons" aria-hidden="true">
      <svg viewBox="0 0 16 16"><path fill="#d0262d" d="M3.5 1.5l2.5 0 1 3.5-1.6 1.1a8 8 0 0 0 4.5 4.5L11 9l3.5 1v2.5a2 2 0 0 1-2 2A11 11 0 0 1 1.5 3.5a2 2 0 0 1 2-2z"/></svg>
      <svg viewBox="0 0 16 16"><rect x="1" y="3" width="14" height="10" rx="1.5" fill="#d0262d"/><path d="M1.5 4l6.5 5 6.5-5" stroke="#24336e" stroke-width="1.4" fill="none"/></svg>
      <svg viewBox="0 0 16 16"><circle cx="8" cy="8" r="6.5" fill="none" stroke="#d0262d" stroke-width="1.6"/><ellipse cx="8" cy="8" rx="2.8" ry="6.5" fill="none" stroke="#d0262d" stroke-width="1.3"/><path d="M1.5 8h13" stroke="#d0262d" stroke-width="1.3"/></svg>
    </div>
    <ul class="contact-list">
      <li class="phone">555 214 7390</li>
      <li class="email">hello@moxdunereel.com</li>
      <li class="website">www.moxdunereel.com</li>
    </ul>
  </section>

  <section class="card card--back" aria-label="Business card, brand side">
    <div class="brand">
      <span class="brand-mark" aria-hidden="true"></span>
      <p class="brand-name">Mox<br>Dune<br>Reel</p>
    </div>
    <p class="tagline">Shaping Every Mox Ahead</p>
  </section>
</main>
</body>
</html>
```